Law Firm Business Card

This is a business card for a law firm that serves US military and veterans.

The card must have ONLY the following (we want an uncluttered look):

- Company logo (PNG, GIF, JPEG copies uploaded)
- A tagline reading: "a law firm for service members and veterans"
- My name and title: "Martin Kovel" and "Attorney"
- My email: "mart.kovel@bramblecourtlegal.com"
- My number: "855-MOKE-TIB (665-3842)"

We are looking for a clean, simple layout with only the above information, likely printed on a bright white cotton stock. The font of our logo is DIN 1451, and the font used on our website is Helvetica Neue. The color of our logo is #336699, and we probably want the tagline in that color also, and my contact information in a dark grey. Please review our website at www.bramblecourtlegal.com to ensure your card design complements our website style.

Thanks and we look forward to seeing your submissions.

A few notes:

- Two-sided submissions are ok
- Please don't add graphics (scales of justice, judges hammer, etc)

```html
<!DOCTYPE html>
<html lang="en">
<head>
<meta charset="utf-8">
<title>Bramble Court Legal — Business Card</title>
<link href="https://fonts.googleapis.com/css2?family=Crimson+Pro:ital,wght@0,400;0,600;1,400;1,600&display=swap" rel="stylesheet">
<style>
  :root {
    --brand-blue: #2a68cc;
    --card-white: #ffffff;
    --ink: #1c1c1c;
    --rule: #333333;
    --stage: #e9e9e9;
    --on-blue: #ffffff;
  }
  * { box-sizing: border-box; margin: 0; padding: 0; }
  html, body {
    width: 1200px; height: 526px; overflow: hidden;
    background: var(--stage);
    font-family: "Crimson Pro", "Palatino Linotype", serif;
  }
  .stage {
    width: 1200px; height: 526px;
    display: flex; align-items: center; justify-content: center; gap: 80px;
  }
  .card {
    position: relative;
    width: 480px; height: 280px;
    border-radius: 26px;
    overflow: hidden;
    box-shadow: 0 2px 6px rgba(0,0,0,.18);
  }

  /* Front */
  .card--front { background: var(--card-white); }
  .front__brand {
    position: absolute; top: 0; left: 0; right: 0; height: 108px;
    display: flex; align-items: center; justify-content: center; gap: 14px;
  }
  .brand-mark {
    width: 18px; height: 18px; background: var(--brand-blue);
  }
  .brand-name {
    font-weight: 600; font-size: 42px; letter-spacing: .5px;
    color: var(--brand-blue); line-height: 1;
  }
  .front__rule {
    position: absolute; left: 0; right: 0; height: 2px; background: var(--rule);
  }
  .front__rule--top { top: 108px; }
  .front__rule--bottom { top: 220px; }
  .front__band {
    position: absolute; top: 114px; left: 0; right: 0; height: 100px;
    background: var(--brand-blue); color: var(--on-blue);
    display: flex; flex-direction: column; align-items: center; justify-content: center; gap: 3px;
  }
  .person__name { font-style: italic; font-weight: 600; font-size: 25px; line-height: 1.1; }
  .person__title { font-style: normal; font-weight: 400; font-size: 19px; }
  .contact {
    display: flex; align-items: center; gap: 8px;
    font-size: 17px; line-height: 1.2;
  }
  .contact svg { width: 14px; height: 14px; flex: none; }
  .front__tagline {
    position: absolute; top: 222px; bottom: 0; left: 0; right: 0;
    display: flex; align-items: center; justify-content: center;
    font-size: 18px; color: var(--ink);
  }

  /* Back */
  .card--back { background: var(--brand-blue); color: var(--on-blue); }
  .back__brand {
    position: absolute; left: 36px; top: 0; bottom: 0; width: 170px;
    display: flex; flex-direction: column; justify-content: center;
    font-weight: 600; font-size: 44px; line-height: 1.0; color: var(--on-blue);
  }
  .back__message {
    position: absolute; left: 200px; right: 20px; top: 0; bottom: 0;
    display: flex; flex-direction: column; align-items: center; justify-content: center;
    text-align: center; font-style: italic;
  }
  .back__tagline { font-weight: 600; font-size: 26px; line-height: 1.15; }
  .back__url { margin-top: 16px; font-weight: 600; font-size: 18px; }
</style>
</head>
<body>
<main class="stage">

  <section class="card card--front" aria-label="Business card front">
    <div class="front__brand">
      <span class="brand-mark"></span>
      <span class="brand-name">Bramble Court Legal</span>
    </div>
    <div class="front__rule front__rule--top"></div>
    <div class="front__band">
      <p class="person__name">Martin Kovel, <span class="person__title">Attorney</span></p>
      <p class="contact">
        <svg viewBox="0 0 16 16" aria-hidden="true"><circle cx="8" cy="8" r="7.2" fill="none" stroke="currentColor" stroke-width="1.2"/><path d="M5.2 4.2c.4-.3.8-.2 1 .1l.8 1.3c.2.3.1.6-.1.8l-.5.4c.4.9 1.1 1.7 2 2.2l.4-.5c.2-.2.6-.3.8-.1l1.3.8c.3.2.4.7.1 1l-.6.6c-.5.5-1.3.5-2 .1-1.8-1-3.2-2.5-3.9-4.3-.3-.7-.2-1.4.3-1.9z" fill="currentColor"/></svg>
        855-MOKE-TIB (665-3842)
      </p>
      <p class="contact">
        <svg viewBox="0 0 16 16" aria-hidden="true"><rect x="1.5" y="4" width="13" height="9" rx="1" fill="none" stroke="currentColor" stroke-width="1.3"/><path d="M1.8 4.5 8 9.2l6.2-4.7" fill="none" stroke="currentColor" stroke-width="1.3"/></svg>
        mart.kovel@bramblecourtlegal.com
      </p>
    </div>
    <div class="front__rule front__rule--bottom"></div>
    <p class="front__tagline">A Law Firm For Service Members And Veterans</p>
  </section>

  <section class="card card--back" aria-label="Business card back">
    <div class="back__brand">
      <span>Bramble</span>
      <span>Court</span>
      <span>Legal</span>
    </div>
    <div class="back__message">
      <p class="back__tagline">A Law Firm<br>For Service<br>Members &amp; Veterans</p>
      <p class="back__url">www.bramblecourtlegal.com</p>
    </div>
  </section>

</main>
</body>
</html>
```